Real Estate Managemene Company Needs Business Card Design

We have a logo design and just need business cards made now for our business. Please use PDF logo # 3.

Card with Information to be attached shortly.

The card is used for a real estate management company. We will need to add four other employees and their cards.

Industry/Entity Type

Real Estate

Contact Information for Business Card

Tariq Nawabi
President
3187 Thornfield Avenue
Suite A
Westbrook Hills, IL 60847
Phone 630.471.2286
Fax 630.493.7720
Cell 630.517.8043
pvgrop@mailnest.net

Once design is approved we will have four other employees
Omar Nawabi
Operations Manager

Samira Nawabi
Administrative Manager

Faz Nawabi
Principal

We would need to take out the cell # 630.517.8043 out for the remaining three cards.

Requirements
Must have
• Please use logo attached

```html
<!DOCTYPE html>
<html lang="en">
<head>
<meta charset="utf-8">
<title>Crestline Property Management – Business Card</title>
<link href="https://fonts.googleapis.com/css2?family=Arimo:wght@400;700&display=swap" rel="stylesheet">
<style>
  :root {
    --backdrop: #e9e6e1;
    --card: #fbfbfb;
    --card-shade: #eeeeee;
    --ink: #3d3d3d;
    --ink-soft: #6f6f6f;
    --brand-blue: #1f78b4;
    --band-dark: #2a2a2a;
    --rule: #4a4a4a;
  }
  * { box-sizing: border-box; margin: 0; padding: 0; }
  html, body {
    width: 1200px; height: 600px; overflow: hidden;
    background: var(--backdrop);
    font-family: "Arimo", Arial, sans-serif;
  }
  .stage {
    width: 1200px; height: 600px;
    display: flex; align-items: center; justify-content: center;
  }
  .business-card {
    position: relative;
    width: 880px; height: 503px;
    background: radial-gradient(ellipse at 40% 45%, var(--card) 55%, var(--card-shade) 100%);
    box-shadow: 0 10px 30px rgba(0,0,0,.18);
    overflow: hidden;
  }
  .brand {
    position: absolute; left: 70px; top: 0; bottom: 34px; width: 360px;
    display: flex; align-items: center; justify-content: center; gap: 14px;
  }
  .brand-mark { width: 22px; height: 22px; background: var(--brand-blue); flex: none; }
  .brand-name {
    font-size: 30px; font-weight: 400; color: var(--ink-soft);
    line-height: 1.2; letter-spacing: .5px;
  }
  .divider {
    position: absolute; left: 470px; top: 118px; width: 2px; height: 210px;
    background: var(--rule);
  }
  .divider::before {
    content: ""; position: absolute; left: 0; top: 0; width: 2px; height: 34px;
    background: var(--brand-blue);
  }
  .contact {
    position: absolute; left: 512px; top: 118px; color: var(--ink);
  }
  .person-name { font-size: 25px; font-weight: 400; color: var(--brand-blue); }
  .person-title { font-size: 16px; color: var(--ink-soft); margin-top: 4px; }
  .contact-lines { list-style: none; margin-top: 40px; }
  .contact-lines li {
    display: flex; align-items: center; gap: 12px;
    font-size: 16px; line-height: 24px; color: var(--ink-soft);
  }
  .contact-lines svg { width: 15px; height: 15px; fill: var(--brand-blue); flex: none; }
  .address { margin-top: 26px; font-size: 17px; line-height: 25px; color: var(--ink); }
  .edge-band {
    position: absolute; left: 0; right: 0; bottom: 0; height: 34px;
  }
</style>
</head>
<body>
<main class="stage">
  <article class="business-card">
    <div class="brand">
      <span class="brand-mark"></span>
      <span class="brand-name">Crestline<br>Property Management</span>
    </div>

    <div class="divider"></div>

    <section class="contact">
      <h1 class="person-name">Tariq Nawabi</h1>
      <p class="person-title">President</p>
      <ul class="contact-lines">
        <li>
          <svg viewBox="0 0 16 16" aria-hidden="true"><rect x="1" y="1" width="14" height="14" rx="2"/><rect x="4" y="4" width="8" height="2" fill="#fff"/><rect x="4" y="8" width="8" height="4" fill="#fff"/></svg>
          630.471.2286
        </li>
        <li>
          <svg viewBox="0 0 16 16" aria-hidden="true"><rect x="4" y="1" width="8" height="5"/><rect x="1" y="6" width="14" height="8" rx="1.5"/><rect x="4" y="9" width="8" height="2" fill="#fff"/></svg>
          630.493.7720
        </li>
        <li>
          <svg viewBox="0 0 16 16" aria-hidden="true"><rect x="4" y="1" width="8" height="14" rx="1.5"/><rect x="5.5" y="3" width="5" height="8" fill="#fff"/></svg>
          630.517.8043
        </li>
        <li>
          <svg viewBox="0 0 16 16" aria-hidden="true"><rect x="1" y="3" width="14" height="10" rx="1"/><path d="M1.5 3.8 8 9l6.5-5.2" fill="none" stroke="#fff" stroke-width="1.4"/></svg>
          pvgrop@mailnest.net
        </li>
      </ul>
      <p class="address">3187 Thornfield Avenue Suite A<br>Westbrook Hills, IL 60847</p>
    </section>

    <svg class="edge-band" viewBox="0 0 880 34" preserveAspectRatio="none" aria-hidden="true">
      <polygon points="0,0 560,0 545,34 0,34" fill="var(--band-dark)"/>
      <polygon points="568,0 580,0 565,34 553,34" fill="var(--band-dark)"/>
      <polygon points="588,0 880,0 880,34 573,34" fill="var(--brand-blue)"/>
    </svg>
  </article>
</main>
</body>
</html>
```